Drop off piece

I am working on a drop off flier to leave at gun stores that introduces Corven Ammunition and our prices. They will be printed on quarter sheets of letter paper. So the size will be 4.25 x 5.5 inches. Relatively small. I am going to attach what I have done. No one likes the script that has looked at it so that needs to be changed, Do your thing

```html
<!DOCTYPE html>
<html lang="en">
<head>
<meta charset="utf-8">
<title>Corven Ammunition – Drop Off Flier</title>
<link href="https://fonts.googleapis.com/css2?family=Montserrat:wght@400;500;600;700;800&display=swap" rel="stylesheet">
<style>
  :root {
    --navy-deep: #0f1f5c;
    --navy: #1b3386;
    --navy-band: #16286e;
    --red: #d8232a;
    --white: #ffffff;
    --paper: #eceef3;
    --ink: #1c2340;
    --muted: #c9d2ee;
    --stage: #dcdde0;
  }
  * { box-sizing: border-box; margin: 0; padding: 0; }
  html, body { width: 880px; height: 1200px; overflow: hidden; }
  body {
    background: var(--stage);
    font-family: "Montserrat", Arial, sans-serif;
    color: var(--ink);
  }
  .flier {
    position: relative;
    width: 880px;
    height: 1200px;
    background: var(--paper);
    overflow: hidden;
  }

  /* Header */
  .header {
    position: absolute; left: 0; top: 0;
    width: 880px; height: 580px;
    background: linear-gradient(180deg, var(--navy-deep) 0%, var(--navy) 60%, #22409a 100%);
    color: var(--white);
  }
  .brand {
    position: absolute; left: 60px; top: 110px;
    display: flex; align-items: center; gap: 18px;
  }
  .brand-dot {
    width: 30px; height: 30px; border-radius: 50%;
    background: var(--red);
  }
  .brand-name {
    font-weight: 800; font-size: 44px; line-height: 1.05;
    letter-spacing: 1px; color: var(--white);
  }
  .emblem {
    position: absolute; left: 570px; top: 50px;
    width: 220px; height: 220px;
    border-radius: 50%;
    background: radial-gradient(circle at 50% 45%, #ffffff 0%, #e9ecf5 45%, #c9343a 70%, #1e3a8f 100%);
  }

  .intro {
    position: absolute; left: 60px; top: 340px;
    width: 780px;
    display: grid; grid-template-columns: 380px 400px;
  }
  .intro h2 {
    font-weight: 500; font-size: 32px; letter-spacing: 1px;
    line-height: 1; margin-bottom: 24px; white-space: nowrap;
  }
  .intro ul { list-style: none; }
  .intro li {
    position: relative; padding-left: 26px;
    font-size: 16px; font-weight: 500; letter-spacing: 1.5px;
    line-height: 32px; color: var(--muted); white-space: nowrap;
  }
  .intro li::before {
    content: ""; position: absolute; left: 2px; top: 12px;
    width: 9px; height: 9px; background: var(--red);
  }

  /* Offerings */
  .offerings {
    position: absolute; left: 0; top: 580px;
    width: 880px; height: 470px;
    background: linear-gradient(180deg, #ffffff 0%, var(--paper) 100%);
  }
  .offerings-title {
    display: flex; align-items: center; justify-content: center; gap: 24px;
    margin-top: 38px;
  }
  .offerings-title h2 {
    font-weight: 500; font-size: 40px; letter-spacing: 2px; color: var(--ink);
  }
  .title-rule { display: flex; align-items: center; }
  .title-rule span { width: 110px; height: 2px; background: var(--red); }
  .price-table {
    margin: 34px 0 0 60px;
    border-collapse: collapse;
    width: 760px;
  }
  .price-table th {
    text-align: left; font-weight: 600; font-size: 18px;
    letter-spacing: 1.5px; color: var(--red);
    padding-bottom: 14px;
    border-bottom: 2px solid var(--red);
  }
  .price-table td {
    font-size: 17px; font-weight: 500; letter-spacing: 1px;
    color: var(--ink); height: 49px;
    border-bottom: 1px solid #d4d8e3;
  }
  .price-table .col-ammo { width: 330px; }
  .price-table .col-retail { width: 130px; }

  /* Contact footer */
  .contact {
    position: absolute; left: 0; top: 1070px;
    width: 880px; height: 130px;
    display: flex;
  }
  .contact-icons {
    width: 130px; background: var(--red);
    display: flex; flex-direction: column; justify-content: center; align-items: center; gap: 14px;
  }
  .contact-lines {
    flex: 1; background: var(--navy-band); color: var(--white);
    display: flex; flex-direction: column; justify-content: center;
    padding-left: 40px; gap: 10px;
  }
  .contact-lines p {
    font-weight: 600; font-size: 26px; letter-spacing: 2px;
  }
</style>
</head>
<body>
<main class="flier">
  <header class="header">
    <div class="brand">
      <span class="brand-dot"></span>
      <span class="brand-name">CORVEN<br>AMMUNITION</span>
    </div>
    <div class="emblem" role="img" aria-label="Shield emblem with crossed flags and stars"></div>

    <section class="intro">
      <div class="intro-col">
        <h2>OUR COMPANY</h2>
        <ul>
          <li>VETERAN OWNED</li>
          <li>FAMILY RUN</li>
          <li>MADE IN MARLOW CREEK, NC</li>
          <li>FOUR NC COMPONETS</li>
        </ul>
      </div>
      <div class="intro-col">
        <h2>OUR AMMUNITION</h2>
        <ul>
          <li>HIGHEST QUALITY COMPONENTS</li>
          <li>SUPERIOR ACCURACY</li>
          <li>CLEAN BURNING</li>
          <li>CONSITENTCEY</li>
        </ul>
      </div>
    </section>
  </header>

  <section class="offerings">
    <div class="offerings-title">
      <div class="title-rule"><span></span></div>
      <h2>OUR OFFERINGSS</h2>
      <div class="title-rule"><span></span></div>
    </div>
    <table class="price-table">
      <thead>
        <tr>
          <th class="col-ammo">AMMUNITION</th>
          <th class="col-retail">RETAIL</th>
          <th>WHOLESALE</th>
        </tr>
      </thead>
      <tbody>
        <tr><td>9MM 115GR RN COATED</td><td>$25.95</td><td>$415.20 / 1,000 ROUNDS</td></tr>
        <tr><td>9MM 124GR RN COATED</td><td>$26.95</td><td>$431.20 / 1,000 ROUNDS</td></tr>
        <tr><td>9MM 147GR RN COATED</td><td>$26.95</td><td>$431.20 / 1,000 ROUNDS</td></tr>
        <tr><td>9MM 90GR T-CORE HP</td><td>$20.95</td><td>$16.76 / 20 ROUNDS</td></tr>
        <tr><td>9MM 115GR KDX HP</td><td>$20.95</td><td>$16.76 / 20 ROUNDS</td></tr>
        <tr><td>9MM 124GR T-CORE HP</td><td>$20.95</td><td>$16.76 / 20 ROUNDS</td></tr>
      </tbody>
    </table>
  </section>

  <footer class="contact">
    <div class="contact-icons">
      <svg width="34" height="34" viewBox="0 0 24 24" aria-hidden="true">
        <path fill="#fff" d="M6.6 10.8a15.1 15.1 0 0 0 6.6 6.6l2.2-2.2c.3-.3.7-.4 1-.2 1.1.4 2.3.6 3.6.6.6 0 1 .4 1 1V20c0 .6-.4 1-1 1C10.6 21 3 13.4 3 4c0-.6.4-1 1-1h3.5c.6 0 1 .4 1 1 0 1.3.2 2.5.6 3.6.1.3 0 .7-.2 1z"/>
      </svg>
      <svg width="34" height="34" viewBox="0 0 24 24" aria-hidden="true">
        <rect x="3" y="6" width="18" height="12" rx="1.5" fill="none" stroke="#fff" stroke-width="2"/>
        <path d="M3.5 7l8.5 6 8.5-6" fill="none" stroke="#fff" stroke-width="2"/>
      </svg>
    </div>
    <div class="contact-lines">
      <p>CALL 864-555-0142</p>
      <p>BEN@CORVENAMMUNITION.COM</p>
    </div>
  </footer>
</main>
</body>
</html>
```